Stationary Design for Landscaping & Cleaning Business

Our landscaping and cleaning business need a stationary design, we would like separate designs for each business that match.
We want a simple yet bold design, using colours of our logos.
We are re designing our business so we need a more professional and modern look.
We don't want any extra words, just the basic contact details.
Name, address, phone number, email, abn and the usual customer details.
We would like to see examples for all stationary and both names.

Target Market(s)

No target market

Industry/Entity Type

Business

Font styles to use
Sans Serif

Colors
ffffff
000000

Requirements
Must have
• Business card, letterhead and envelope design.
Nice to have
• Lines and coloured areas
Should not have
• No extra pictures

```html
<!DOCTYPE html>
<html lang="en">
<head>
<meta charset="utf-8">
<title>Quillfern Gardens – Stationery</title>
<link rel="stylesheet" href="https://fonts.googleapis.com/css2?family=Carlito:wght@400;700&family=Roboto:wght@400;500&display=swap">
<style>
  :root {
    --stage: #a3a3a3;
    --paper: #ffffff;
    --ink: #1c1c1c;
    --black: #0b0b0d;
    --green: #8dc63f;
    --shadow: 6px 8px 10px rgba(0,0,0,0.35);
  }
  * { margin: 0; padding: 0; box-sizing: border-box; }
  html, body { width: 1200px; height: 640px; overflow: hidden; background: var(--stage); }
  .canvas { position: relative; width: 1200px; height: 640px; font-family: "Roboto", Arial, sans-serif; color: var(--ink); }
  .sheet { position: absolute; background: var(--paper); box-shadow: var(--shadow); overflow: hidden; }

  .brand { font-family: "Roboto", Arial, sans-serif; font-weight: 500; letter-spacing: -0.3px; color: var(--ink); white-space: nowrap; line-height: 1; }
  .brand--light { color: var(--green); }

  .icons { display: none; }
  .contact { font-size: 5.6px; line-height: 1.55; color: var(--ink); }
  .contact li { list-style: none; display: flex; align-items: center; gap: 3px; }
  .contact svg { width: 5px; height: 5px; fill: var(--green); flex: none; }
  .contact .gap { margin-top: 5px; }
  .address { font-size: 5.6px; line-height: 1.6; color: var(--green); }

  /* Letterhead */
  .letterhead { left: 26px; top: 32px; width: 412px; height: 582px; font-family: "Carlito", Calibri, sans-serif; }
  .letterhead .brand { position: absolute; left: 33px; top: 30px; font-size: 17px; }
  .letterhead .contact { position: absolute; left: 320px; top: 27px; padding-left: 5px; border-left: 0.8px solid var(--green); font-family: "Roboto", Arial, sans-serif; font-size: 4.8px; }
  .letterhead .abn { color: var(--green); margin-top: 2px; }
  .letter { position: absolute; left: 32px; top: 118px; width: 345px; font-size: 7.6px; line-height: 14.2px; color: var(--ink); }
  .letter .recipient { font-weight: 700; margin-top: 0; }
  .letter .recipient span:first-child { font-weight: 400; }
  .letter p + p { margin-top: 14px; }
  .signoff { position: absolute; left: 32px; top: 422px; font-size: 7.6px; line-height: 14.2px; color: var(--ink); }
  .signature { width: 105px; height: 34px; margin: 6px 0 8px; background: linear-gradient(90deg, #e9e9e9, #f4f4f4); }
  .letterhead .waves { position: absolute; left: 0; bottom: 0; width: 412px; height: 70px; }

  /* Business cards */
  .card { top: 32px; width: 222px; height: 138px; }
  .card .brand { font-size: 12.5px; position: absolute; }
  .card .person { position: absolute; }
  .card .person strong { display: block; font-weight: 500; font-size: 8px; color: var(--green); }
  .card .person small { display: block; font-size: 4.4px; margin-top: 2px; }
  .card--left { left: 463px; }
  .card--left .contact { position: absolute; left: 14px; top: 56px; }
  .card--left .address { position: absolute; left: 14px; top: 115px; }
  .card--left .brand { right: 16px; top: 80px; }
  .card--left .person { right: 16px; top: 103px; text-align: right; }
  .card--right { left: 706px; }
  .card--right .brand { left: 20px; top: 80px; }
  .card--right .person { left: 20px; top: 103px; }
  .card--right .contact { position: absolute; left: 137px; top: 55px; }
  .card--right .address { position: absolute; left: 137px; top: 113px; }
  .card--back { left: 950px; width: 221px; background: var(--black); }
  .card--back .brand { left: 21px; top: 102px; font-size: 13px; }

  /* Envelopes */
  .envelope { left: 463px; width: 430px; }
  .envelope--front { top: 236px; height: 172px; }
  .envelope--front .brand { position: absolute; left: 11px; top: 14px; font-size: 10px; }
  .envelope--front .contact { position: absolute; left: 11px; top: 30px; font-size: 4.4px; }
  .envelope--front .sender { font-weight: 500; font-size: 4.4px; line-height: 1.5; margin-top: 2px; }
  .envelope--back { top: 439px; height: 171px; }
  .envelope--back .flap { position: absolute; left: 0; top: 0; width: 430px; height: 48px; }
</style>
</head>
<body>
<svg class="icons" aria-hidden="true">
  <symbol id="i-phone" viewBox="0 0 10 10"><path d="M2 0h2l1 3-1.5 1a6 6 0 0 0 2.5 2.5L7 5l3 1v2a2 2 0 0 1-2 2A8 8 0 0 1 0 2a2 2 0 0 1 2-2z"/></symbol>
  <symbol id="i-fax" viewBox="0 0 10 10"><rect x="2" y="0" width="6" height="4"/><rect x="0" y="4" width="10" height="6" rx="1"/></symbol>
  <symbol id="i-mail" viewBox="0 0 10 10"><path d="M0 2h10v6H0z M0 2l5 4 5-4"/></symbol>
  <symbol id="i-web" viewBox="0 0 10 10"><circle cx="5" cy="5" r="5"/><circle cx="5" cy="5" r="2.5" fill="#fff"/></symbol>
</svg>

<main class="canvas">
  <section class="sheet letterhead" aria-label="Letterhead">
    <div class="brand">Quillfern Gardens</div>
    <ul class="contact">
      <li><svg><use href="#i-phone"/></svg>00 0000 5217</li>
      <li><svg><use href="#i-fax"/></svg>00 0000 5217</li>
      <li class="gap"><svg><use href="#i-mail"/></svg>hello@mailbox.com.au</li>
      <li><svg><use href="#i-web"/></svg>www.sitelink.com.au</li>
      <li class="abn gap">ABN: 00 512 348 000</li>
    </ul>
    <div class="letter">
      <p class="recipient"><span>To</span><br>Mr. Owen Brooks<br>Lorem Ipsum is simply a dummy text</p>
      <p>dummy text of the printing and typesetting industry. Lorem Ipsum has been the industry's standard dummy text ever since the 1500s, when an unknown printer took a galley of type and scrambled it to make a type specimen book. It has survived not only five centuries, but also the leap into electronic typesetting, remaining essentially unchanged. It was popularised in the 1960s with the release</p>
      <p>It is a long established fact that a reader will be distracted by the readable content of a page when lookidesktop publishing packages and web page editors now use Lorem Ipsum as their default model text, and a search for 'lorem ipsum' will uncover many web sites still in their infancy. Various versions have evolved over the years, sometimes by accident, sometimes on purpose (injected humour and the like).</p>
      <p>a Latin professor at Brindlecote College on the ridge, looked up one of the more obscure Latin words, consectetur, from a Lorem Ipsum passage, and going through the cites of the word in classical literature, discovered the undoubtable source. Lorem Ipsum comes from sections 1.10.32 and 1.10.33 of "de Finibus Bonorum et Malorum" (The Extremes of Good and Evil) by Quintor Vessa, written in 45 BC. This book</p>
    </div>
    <div class="signoff">
      <div>Lorem Ipsum</div>
      <div class="signature" role="img" aria-label="Handwritten signature"></div>
      <div>Lorem Ipsum is a dummy</div>
    </div>
    <svg class="waves" viewBox="0 0 412 70" preserveAspectRatio="none" aria-hidden="true">
      <path d="M0 46 C120 10 260 0 412 8 L412 70 L0 70 Z" fill="var(--black)"/>
      <path d="M0 52 C140 26 280 24 412 26 L412 70 L0 70 Z" fill="var(--green)"/>
      <path d="M0 66 C150 50 290 50 412 48 L412 70 L0 70 Z" fill="var(--black)"/>
    </svg>
  </section>

  <section class="sheet card card--left" aria-label="Business card front">
    <ul class="contact">
      <li><svg><use href="#i-phone"/></svg>00 0000 5217</li>
      <li><svg><use href="#i-fax"/></svg>00 0000 5217</li>
      <li class="gap"><svg><use href="#i-mail"/></svg>hello@mailbox.com.au</li>
      <li><svg><use href="#i-web"/></svg>www.sitelink.com.au</li>
    </ul>
    <div class="address">Suite 8, 12 Elm St.<br>Town Name, PB 4210</div>
    <div class="brand">Quillfern Gardens</div>
    <div class="person"><strong>Daniel Hart</strong><small>Managing Director</small></div>
  </section>

  <section class="sheet card card--right" aria-label="Business card alternate front">
    <div class="brand">Quillfern Gardens</div>
    <div class="person"><strong>Daniel Hart</strong><small>Managing Director</small></div>
    <ul class="contact">
      <li><svg><use href="#i-phone"/></svg>00 0000 5217</li>
      <li><svg><use href="#i-fax"/></svg>00 0000 5217</li>
      <li class="gap"><svg><use href="#i-mail"/></svg>hello@mailbox.com.au</li>
      <li><svg><use href="#i-web"/></svg>www.sitelink.com.au</li>
    </ul>
    <div class="address">Suite 8, 12 Elm St.<br>Town Name, PB 4210</div>
  </section>

  <section class="sheet card card--back" aria-label="Business card back">
    <div class="brand brand--light">Quillfern Gardens</div>
  </section>

  <section class="sheet envelope envelope--front" aria-label="Envelope front">
    <div class="brand">Quillfern Gardens</div>
    <ul class="contact">
      <li><svg><use href="#i-mail"/></svg>hello@mailbox.com.au</li>
      <li><svg><use href="#i-web"/></svg>www.sitelink.com.au</li>
      <li class="sender">Suite 8, 12 Elm St.<br>Town Name, PB 4210</li>
    </ul>
  </section>

  <section class="sheet envelope envelope--back" aria-label="Envelope back">
    <svg class="flap" viewBox="0 0 430 48" aria-hidden="true">
      <path d="M0 0 H430 L406 44 Q404 48 398 48 H32 Q26 48 24 44 Z" fill="var(--black)"/>
    </svg>
  </section>
</main>
</body>
</html>
```